Readable, Vibrant Large Shop Front Poster for Tutoring School.

Uncluttered design for the windows of our Business.
It needs to be readable from a distance.
It will be split across two windows. I've uploaded a picture of the premises. The poster is unfortunately split in two- see the shopfront photo - It will be in the two Square windows where the balloons are now.
I've also uploaded our logo which will be used as signage/ on the roof and would like the posters to tie in with it.

What we want to stand out
Over all :
That we are a Tutoring School Specializing in Secondary/KTR Studies

On the left hand side:
- 1 hour lessons are $20 with no joining fees or contracts (casual week to week bookings)

The right hand side:
-Weekly Lessons no contracts
-Summer School
-Holiday Program
-Workshops
-KTR EXAM PREP

Need B0 size (1000mm x 1414mm)

Requirements
Must have
• It must have large clear writing.
Nice to have
• a border top and bottom of the logo swirls, We don't need the business name on this poster.
Should not have
• Not a fan of Purple or Lime Green.

```html
<!DOCTYPE html>
<html lang="en">
<head>
<meta charset="utf-8">
<title>Tutoring School Window Poster</title>
<link href="https://fonts.googleapis.com/css2?family=Bebas+Neue&family=Montserrat:wght@600;800&display=swap" rel="stylesheet">
<style>
  :root {
    --navy: #1b1f2d;
    --magenta: #e0115f;
    --amber: #f9a825;
    --white: #ffffff;
    --ring: #f7a21b;
    --ink: #1b1f2d;
    --book-pink: #f29cc4;
    --book-yellow: #f3d21a;
    --book-orange: #f26b21;
  }
  html, body {
    margin: 0;
    padding: 0;
    width: 1200px;
    height: 851px;
    overflow: hidden;
    background: var(--navy);
  }
  .poster {
    position: relative;
    width: 1200px;
    height: 851px;
    background: var(--navy);
    color: var(--white);
    font-family: "Bebas Neue", sans-serif;
    overflow: hidden;
    white-space: nowrap;
  }
  .swirl-border {
    position: absolute;
    left: 0;
    width: 1200px;
    height: 40px;
    background: linear-gradient(90deg, #f5c518, #ef3b6b, #2ec4e6, #f26b21, #e0115f, #f5c518, #2ec4e6, #f26b21, #ef3b6b, #f5c518);
    opacity: 0.9;
  }
  .swirl-border--top { top: 21px; }
  .swirl-border--bottom { top: 782px; }

  .headline {
    position: absolute;
    left: 0;
    top: 88px;
    width: 1200px;
    height: 75px;
    margin: 0;
    background: var(--magenta);
    font-family: "Montserrat", sans-serif;
    font-weight: 800;
    font-size: 56px;
    line-height: 78px;
    text-align: center;
    letter-spacing: 0.5px;
  }
  .subheadline {
    position: absolute;
    left: 0;
    top: 188px;
    width: 1200px;
    margin: 0;
    font-size: 86px;
    line-height: 92px;
    text-align: center;
    font-weight: 400;
    text-shadow: 0 3px 4px rgba(0,0,0,0.5);
  }

  .price-label {
    position: absolute;
    left: 0;
    top: 298px;
    width: 407px;
    height: 63px;
    background: var(--amber);
    font-size: 60px;
    line-height: 68px;
    text-align: right;
    box-sizing: border-box;
    padding-right: 8px;
  }
  .price {
    position: absolute;
    left: 0;
    top: 374px;
    width: 407px;
    margin: 0;
    font-size: 98px;
    line-height: 98px;
    text-align: right;
    font-weight: 400;
  }
  .terms {
    position: absolute;
    left: 0;
    top: 474px;
    width: 408px;
    height: 58px;
  }
  .casual {
    position: absolute;
    left: 20px;
    top: 551px;
    width: 388px;
    font-size: 33px;
    line-height: 38px;
    text-align: center;
  }

  .brand {
    position: absolute;
    left: 40px;
    top: 608px;
    width: 340px;
    text-align: center;
  }
  .brand-dot {
    display: block;
    width: 84px;
    height: 84px;
    margin: 0 auto 26px;
    border-radius: 50%;
    background: var(--magenta);
  }
  .brand-name {
    font-family: "Montserrat", sans-serif;
    font-weight: 600;
    font-size: 32px;
    letter-spacing: 4px;
    line-height: 34px;
  }

  .book-stack {
    position: absolute;
    left: 463px;
    top: 291px;
    width: 271px;
    height: 463px;
    border-radius: 10px;
    background: linear-gradient(180deg, #4d4d4d 0%, #4d4d4d 16%, var(--book-pink) 17%, var(--book-pink) 28%, var(--book-yellow) 29%, var(--book-yellow) 45%, var(--book-orange) 46%, var(--book-orange) 58%, var(--book-pink) 59%, var(--book-pink) 70%, var(--book-yellow) 71%, var(--book-yellow) 84%, var(--book-orange) 85%, var(--book-orange) 100%);
  }

  .service {
    position: absolute;
    text-align: center;
    font-size: 31px;
    line-height: 34px;
  }
  .service-icon {
    display: block;
    margin: 0 auto;
    border-radius: 50%;
    background: var(--white);
    border: 5px solid var(--ring);
    box-sizing: border-box;
  }
  .service-icon svg { display: block; width: 100%; height: 100%; }
  .service--feature {
    left: 783px;
    top: 292px;
    width: 400px;
    font-size: 37px;
    line-height: 40px;
  }
  .service--feature .service-icon { width: 82px; height: 82px; margin-bottom: 10px; }
  .service--small .service-icon { width: 66px; height: 66px; margin-bottom: 10px; }
  .service--summer { left: 769px; top: 472px; width: 200px; }
  .service--holiday { left: 986px; top: 472px; width: 200px; }
  .service--workshops { left: 769px; top: 622px; width: 200px; }
  .service--exam { left: 986px; top: 622px; width: 200px; }
</style>
</head>
<body>
<main class="poster">
  <div class="swirl-border swirl-border--top" role="img" aria-label="Border of colourful swirl motifs"></div>

  <h1 class="headline">THAT WE ARE A TUTORING SCHOOL</h1>
  <h2 class="subheadline">SPECIALIZING IN SECONDARY / KTR STUDIES</h2>

  <div class="price-label">1 HOUR LESSONS ARE</div>
  <p class="price">$20 WITH NO</p>

  <svg class="terms" viewBox="0 0 408 58" aria-label="With no joining fees or contracts">
    <polygon points="0,0 262,0 252,34 0,34" fill="var(--magenta)"/>
    <polygon points="246,22 408,22 408,56 236,56" fill="var(--magenta)"/>
    <line x1="266" y1="-4" x2="234" y2="58" stroke="var(--magenta)" stroke-width="3"/>
    <text x="22" y="28" fill="#fff" font-family="Bebas Neue, sans-serif" font-size="29">WITH NO JOINING FEES</text>
    <text x="256" y="50" fill="#fff" font-family="Bebas Neue, sans-serif" font-size="29">OR CONTRACTS</text>
  </svg>

  <div class="casual">( CASUAL WEEK TO WEEK BOOKINGS )</div>

  <div class="brand">
    <span class="brand-dot"></span>
    <div class="brand-name">BRIGHT DESK</div>
  </div>

  <div class="book-stack" role="img" aria-label="Illustration of a stack of coloured books topped with a graduation cap"></div>

  <div class="service service--feature">
    <span class="service-icon">
      <svg viewBox="0 0 72 72" aria-hidden="true">
        <rect x="26" y="20" width="28" height="20" fill="none" stroke="#1b1f2d" stroke-width="3"/>
        <circle cx="21" cy="30" r="4" fill="#1b1f2d"/>
        <rect x="17" y="35" width="8" height="16" fill="#1b1f2d"/>
      </svg>
    </span>
    WEEKLY LESSONS NO CONTRACTS
  </div>

  <div class="service service--small service--summer">
    <span class="service-icon">
      <svg viewBox="0 0 56 56" aria-hidden="true">
        <circle cx="33" cy="22" r="7" fill="none" stroke="#1b1f2d" stroke-width="3"/>
        <polygon points="10,32 26,26 42,32 26,38" fill="#1b1f2d"/>
      </svg>
    </span>
    SUMMER SCHOOL
  </div>

  <div class="service service--small service--holiday">
    <span class="service-icon">
      <svg viewBox="0 0 56 56" aria-hidden="true">
        <circle cx="28" cy="18" r="4" fill="#1b1f2d"/>
        <circle cx="18" cy="31" r="3.5" fill="#1b1f2d"/>
        <circle cx="28" cy="31" r="3.5" fill="#1b1f2d"/>
        <circle cx="38" cy="31" r="3.5" fill="#1b1f2d"/>
        <rect x="12" y="36" width="32" height="5" fill="#1b1f2d"/>
      </svg>
    </span>
    HOLIDAY PROGRAM
  </div>

  <div class="service service--small service--workshops">
    <span class="service-icon">
      <svg viewBox="0 0 56 56" aria-hidden="true">
        <polygon points="28,16 40,40 16,40" fill="#1b1f2d"/>
        <line x1="14" y1="14" x2="14" y2="40" stroke="#1b1f2d" stroke-width="2"/>
        <line x1="42" y1="14" x2="42" y2="40" stroke="#1b1f2d" stroke-width="2"/>
      </svg>
    </span>
    WORKSHOPS
  </div>

  <div class="service service--small service--exam">
    <span class="service-icon">
      <svg viewBox="0 0 56 56" aria-hidden="true">
        <rect x="17" y="14" width="20" height="26" fill="none" stroke="#1b1f2d" stroke-width="3"/>
        <line x1="21" y1="22" x2="33" y2="22" stroke="#1b1f2d" stroke-width="2"/>
        <line x1="21" y1="28" x2="33" y2="28" stroke="#1b1f2d" stroke-width="2"/>
        <line x1="30" y1="42" x2="42" y2="28" stroke="#1b1f2d" stroke-width="4"/>
      </svg>
    </span>
    KTR EXAM PREP
  </div>

  <div class="swirl-border swirl-border--bottom" role="img" aria-label="Border of colourful swirl motifs"></div>
</main>
</body>
</html>
```